DL Flyer & Matching business card

I have done a mock DL flyer, i am happy with the back ground and layout. i need you to fix and format fonts so i looks better...i am happy for you to change icons and fonts but not the layout...i also want a business card to match,, with out all the text obviously but the same background as DL flyer so they match...

My colours are
Blue
PMS coated 2192c
PMS uncoated 2995u
CMYK C80: M10: Y0: K0
RGB R0: G163: B224
HEX #00A3E0

Grey/Black
PMS coated 7540C
PMS uncoated Cool grey 11U
CMYK C0: M0: Y0: K77
RGB R95: G96: B98
HEX #5F6062

Reason: need more time

Industry/Entity Type

Finance

Font styles to use
Sans Serif

Colors

Designer to choose colors to be used in the design.

Requirements
Must have
• my colours, i have the design, just need proper font formatting .
• Blue
• PMS coated 2192c
• PMS uncoated 2995u
• CMYK C80: M10: Y0: K0
• RGB R0: G163: B224
• HEX #00A3E0
• Grey/Black
• PMS coated 7540C
• PMS uncoated Cool grey 11U
• CMYK C0: M0: Y0: K77
• RGB R95: G96: B98
• HEX #5F6062

```html
<!DOCTYPE html>
<html lang="en">
<head>
<meta charset="UTF-8">
<title>Northfield Lending Partners – Business Card</title>
<link rel="stylesheet" href="https://fonts.googleapis.com/css2?family=Montserrat:wght@400;500;600;700;800&display=swap">
<style>
  :root {
    --brand-blue: #00A3E0;
    --brand-charcoal: #2d2e30;
    --brand-grey: #5F6062;
    --paper: #ffffff;
    --backdrop: #d6d7d9;
    --text-light: #eceef0;
    --text-muted: #b9bbbe;
  }
  html, body {
    margin: 0;
    padding: 0;
    width: 1200px;
    height: 1200px;
    overflow: hidden;
    background: var(--backdrop);
    font-family: "Montserrat", sans-serif;
  }
  .canvas {
    position: relative;
    width: 1200px;
    height: 1200px;
  }
  .business-card {
    position: absolute;
    left: 100px;
    top: 310px;
    width: 1000px;
    height: 580px;
    background: var(--paper);
    box-shadow: 0 18px 40px rgba(0,0,0,0.18);
    overflow: hidden;
  }
  .card-background {
    position: absolute;
    inset: 0;
    width: 100%;
    height: 100%;
  }
  .brand-name {
    position: absolute;
    left: 380px;
    top: 82px;
    width: 460px;
    margin: 0;
    color: var(--brand-blue);
    font-weight: 700;
    font-size: 36px;
    line-height: 1.1;
    letter-spacing: 1px;
    text-transform: uppercase;
    text-align: right;
    white-space: nowrap;
  }
  .service-tagline {
    position: absolute;
    left: 372px;
    top: 206px;
    width: 380px;
    margin: 0;
    color: var(--paper);
    font-weight: 600;
    font-size: 12.5px;
    line-height: 1.45;
    letter-spacing: 0.6px;
    text-align: center;
    text-transform: uppercase;
  }
  .holder {
    position: absolute;
    left: 70px;
    top: 292px;
  }
  .holder-name {
    margin: 0;
    color: var(--brand-blue);
    font-weight: 800;
    font-size: 50px;
    line-height: 1;
    letter-spacing: 1px;
  }
  .holder-role {
    margin: 6px 0 0 2px;
    color: var(--text-muted);
    font-weight: 500;
    font-size: 16px;
  }
  .contact-list {
    position: absolute;
    left: 420px;
    top: 300px;
    margin: 0;
    padding: 0;
    list-style: none;
  }
  .contact-item {
    display: flex;
    align-items: center;
    height: 40px;
    color: var(--text-light);
    font-weight: 500;
    font-size: 22px;
    letter-spacing: 0.3px;
  }
  .contact-icon {
    width: 24px;
    height: 24px;
    margin-right: 16px;
    flex: none;
  }
</style>
</head>
<body>
<div class="canvas">
  <section class="business-card" aria-label="Business card front">
    <svg class="card-background" viewBox="0 0 1000 580" aria-hidden="true">
      <rect x="0" y="0" width="1000" height="580" fill="var(--paper)"/>
      <rect class="dark-panel" x="0" y="248" width="1000" height="332" fill="var(--brand-charcoal)"/>
      <rect class="panel-edge" x="0" y="242" width="1000" height="7" fill="var(--brand-blue)"/>
      <polygon class="tagline-tab" points="335,262 362,196 768,196 800,262 760,262" fill="var(--brand-blue)"/>
      <polygon class="tagline-tab-base" points="335,262 800,262 780,274 345,274" fill="var(--brand-blue)"/>
      <rect class="bottom-stripe" x="0" y="556" width="1000" height="14" fill="var(--brand-blue)"/>
      <rect x="0" y="570" width="1000" height="10" fill="var(--paper)"/>
      <line class="contact-divider" x1="392" y1="300" x2="350" y2="408" stroke="var(--text-light)" stroke-width="2"/>
    </svg>

    <h1 class="brand-name">Northfield Lending<br>Partners</h1>
    <p class="service-tagline">Home Loans | Plant &amp; Equipment | Automotive<br>Business &amp; Commercial | Personal</p>

    <div class="holder">
      <p class="holder-name">NAME</p>
      <p class="holder-role">Designation</p>
    </div>

    <ul class="contact-list">
      <li class="contact-item">
        <svg class="contact-icon" viewBox="0 0 24 24" aria-hidden="true">
          <circle cx="12" cy="12" r="12" fill="var(--brand-blue)"/>
          <path d="M12 5.5a4 4 0 0 0-4 4c0 3 4 8 4 8s4-5 4-8a4 4 0 0 0-4-4z" fill="#fff"/>
          <circle cx="12" cy="9.5" r="1.5" fill="var(--brand-blue)"/>
        </svg>
        8/22 Wattle St Orange NSW 2800
      </li>
      <li class="contact-item">
        <svg class="contact-icon" viewBox="0 0 24 24" aria-hidden="true">
          <circle cx="12" cy="12" r="12" fill="var(--brand-blue)"/>
          <path d="M8.6 6.5l2 2.3-1.2 1.6c.8 1.6 2 2.8 3.6 3.6l1.6-1.2 2.3 2-1.1 2c-4.6-.4-8.4-4.2-8.8-8.8z" fill="#fff"/>
        </svg>
        02 5550 1234/ 0400 555 019
      </li>
      <li class="contact-item">
        <svg class="contact-icon" viewBox="0 0 24 24" aria-hidden="true">
          <circle cx="12" cy="12" r="12" fill="var(--brand-blue)"/>
          <rect x="6" y="8" width="12" height="8.5" rx="1" fill="#fff"/>
          <path d="M6.3 8.4L12 12.6l5.7-4.2" fill="none" stroke="var(--brand-blue)" stroke-width="1.2"/>
        </svg>
        sam@northfieldlending.com.au
      </li>
      <li class="contact-item">
        <svg class="contact-icon" viewBox="0 0 24 24" aria-hidden="true">
          <circle cx="12" cy="12" r="12" fill="var(--brand-blue)"/>
          <rect x="6" y="7" width="12" height="8" rx="1" fill="none" stroke="#fff" stroke-width="1.6"/>
          <path d="M10 17.5h4M12 15v2.5" stroke="#fff" stroke-width="1.6"/>
        </svg>
        www.northfieldlending.com.au
      </li>
    </ul>
  </section>
</div>
</body>
</html>
```